Lone Elm Cattle Website

I need a website for my cattle company. I will be sharing pictures of my herd along with selling my calves individually. I need the following pages:
About
Cattle Sales
Bulls
Cows/Heifers
Gallery
Contact Us

I just uploaded a few pictures, but I have a lot more!

```html
<!DOCTYPE html>
<html lang="en">
<head>
<meta charset="utf-8">
<title>Lone Elm Cattle</title>
<link href="https://fonts.googleapis.com/css2?family=Smokum&family=Roboto:wght@400;500;700&display=swap" rel="stylesheet">
<style>
:root{
  --brown:#4a3320;
  --brown-mid:#5b3f22;
  --brown-dark:#3a2817;
  --cream:#fdf2e4;
  --ink:#2b2b2b;
  --muted:#6b6b6b;
  --white:#ffffff;
  --field:#ececec;
}
*{box-sizing:border-box;margin:0;padding:0}
html,body{width:1200px;height:4461px;overflow:hidden}
body{position:relative;font-family:'Roboto',sans-serif;color:var(--ink);background:var(--white)}
.display{font-family:'Smokum',serif;font-weight:400;letter-spacing:1px;white-space:nowrap}
.btn{position:absolute;display:flex;align-items:center;justify-content:center;gap:8px;background:var(--brown);color:var(--white);font-weight:500;border-radius:30px;font-size:14px;letter-spacing:.3px;white-space:nowrap}
.btn svg{width:14px;height:14px}
.torn{position:absolute;left:0;width:1200px;height:26px}

/* header */
.site-header{position:absolute;top:0;left:0;width:1200px;height:107px;background:var(--white);z-index:3}
.logo-disc{position:absolute;left:107px;top:-25px;width:222px;height:222px;border-radius:50%;background:var(--white);z-index:4;display:flex;align-items:center;justify-content:center;flex-direction:column;gap:8px;padding-top:20px}
.brand-text{font-family:'Smokum',serif;color:var(--brown);font-size:30px;text-align:center;line-height:1}
.brand-dot{width:14px;height:14px;border-radius:50%;background:var(--brown)}
.top-contact{position:absolute;top:12px;display:flex;gap:10px;align-items:center}
.top-contact .ico{width:38px;height:38px;border-radius:50%;background:var(--brown-dark);display:flex;align-items:center;justify-content:center}
.top-contact small{display:block;font-size:11px;color:var(--muted)}
.top-contact b{font-size:14px;font-weight:500;color:var(--ink)}
.top-contact.phone b{font-size:18px;color:var(--brown)}
.nav{position:absolute;top:78px;left:482px;display:flex;gap:26px;font-size:14px;font-weight:500;color:var(--ink)}
.nav .active{color:var(--brown)}

/* hero */
.hero{position:absolute;top:107px;left:0;width:1200px;height:590px;background:linear-gradient(180deg,#93a6bc 0%,#aab5bd 30%,#8d8463 52%,#6d5a3a 75%,#5a4a30 100%)}
.hero h1{position:absolute;top:88px;left:0;width:100%;text-align:center;color:var(--white);font-size:58px;line-height:64px}
.hero p{position:absolute;top:170px;left:350px;width:500px;text-align:center;color:var(--white);font-size:16px;line-height:26px}

/* about */
.about-mark{position:absolute;left:107px;top:757px;width:478px;height:438px;display:flex;flex-direction:column;align-items:center;justify-content:center;gap:18px}
.about-mark .brand-text{font-size:66px}
.about-mark .brand-dot{width:26px;height:26px}
.section-title{color:var(--brown);font-size:40px;line-height:48px}
.about h2{position:absolute;left:650px;top:790px;display:flex;align-items:center;gap:14px}
.about h2 span.rule{display:inline-block;width:72px;height:3px;background:var(--brown-dark)}
.about p{position:absolute;left:650px;width:440px;font-size:14px;line-height:26px;color:var(--muted)}

/* sale */
.sale{position:absolute;top:1290px;left:0;width:1200px;height:615px;background:var(--cream)}
.center-title{position:absolute;left:0;width:100%;text-align:center}
.underline{position:absolute;left:565px;width:70px;height:4px;background:var(--brown-dark)}
.card-photo{position:absolute;top:186px;width:310px;height:222px;border-radius:6px}
.card-body{position:absolute;top:376px;width:282px;height:118px;background:var(--white);border-radius:6px;box-shadow:0 4px 14px rgba(0,0,0,.06);text-align:center;padding-top:22px}
.card-body h3{font-size:17px;font-weight:700;color:var(--ink)}
.card-body p{font-size:12px;color:var(--muted);margin-top:10px;word-spacing:2px;white-space:nowrap}

/* why */
.why{position:absolute;top:1905px;left:0;width:1200px;height:606px;background:var(--brown-mid);color:var(--white)}
.why h2{position:absolute;left:111px;top:100px;font-size:40px;line-height:48px;color:var(--white)}
.why .bar{position:absolute;left:111px;top:158px;width:72px;height:4px;background:var(--white)}
.feature{position:absolute;left:111px;width:500px;display:flex;gap:22px}
.feature .ico{flex:none;width:70px;height:70px;border-radius:50%;background:var(--brown-dark);display:flex;align-items:center;justify-content:center}
.feature h3{font-size:18px;font-weight:700;margin-top:4px}
.feature p{font-size:14px;line-height:22px;margin-top:10px;opacity:.95}
.why-photo{position:absolute;left:680px;top:105px;width:400px;height:400px;border-radius:50%;border:3px solid rgba(255,255,255,.85);background:radial-gradient(circle at 50% 40%,#b8a993 0%,#8b8a68 45%,#55653a 100%)}

/* gallery */
.gallery-tile{position:absolute}

/* contact */
.contact{position:absolute;top:3481px;left:0;width:1200px;height:555px;background:var(--brown-dark);color:var(--white)}
.contact h2{color:var(--white);font-size:38px;line-height:46px}
.info{position:absolute;left:107px;display:flex;gap:20px}
.info .ico{flex:none;width:46px;height:46px;border-radius:50%;border:1.5px solid var(--white);display:flex;align-items:center;justify-content:center}
.info h4{font-size:16px;font-weight:700}
.info p{font-size:14px;line-height:22px;margin-top:4px}
.field{position:absolute;background:var(--field);color:#777;font-size:12px;display:flex;align-items:center;gap:6px;padding-left:16px}
.field.msg{align-items:flex-start;padding-top:20px}

/* footer */
.foot-brand{position:absolute;left:107px;top:4131px;width:234px;height:216px;display:flex;flex-direction:column;align-items:center;justify-content:center;gap:10px}
.foot-brand .brand-text{font-size:36px}
.foot-col{position:absolute;top:4118px}
.foot-col h4{font-size:17px;font-weight:700;color:var(--ink);white-space:nowrap}
.foot-col .rule{width:64px;height:2px;background:var(--brown-dark);margin-top:12px}
.foot-col ul{list-style:none;margin-top:18px;font-size:12px;line-height:26px;color:var(--ink)}
.fc-row{display:flex;gap:14px;align-items:flex-start;font-size:12px;line-height:20px;margin-top:14px}
.fc-row .ico{flex:none;width:26px;height:26px;border-radius:50%;background:var(--brown-dark);display:flex;align-items:center;justify-content:center}
.sub-field{position:absolute;left:836px;top:4234px;width:252px;height:36px;border-radius:20px;background:#ececec;font-size:11px;color:#777;display:flex;align-items:center;padding-left:14px}
.sub-btn{position:absolute;left:1040px;top:4234px;width:48px;height:36px;border-radius:0 20px 20px 0;background:var(--brown-dark);display:flex;align-items:center;justify-content:center}
.social{position:absolute;top:4283px;width:28px;height:28px;border-radius:50%;background:#eeeeee}
.chat{position:absolute;left:1127px;top:4336px;width:40px;height:40px;border-radius:50%;background:var(--brown-dark);display:flex;align-items:center;justify-content:center}
.bottom-bar{position:absolute;top:4399px;left:0;width:1200px;height:62px;background:var(--cream);font-size:13px;color:var(--ink)}
.bottom-bar .left{position:absolute;left:111px;top:22px}
.bottom-bar .right{position:absolute;right:111px;top:22px;word-spacing:2px}
</style>
</head>
<body>

<svg width="0" height="0" style="position:absolute">
  <defs>
    <path id="tornEdge" d="M0 26 L0 12 L18 15 L34 8 L52 13 L70 6 L88 14 L104 9 L124 16 L142 7 L160 12 L178 5 L196 13 L214 9 L232 15 L250 6 L268 12 L288 8 L306 16 L324 7 L342 13 L360 9 L380 15 L398 6 L416 12 L434 8 L454 14 L472 6 L490 13 L508 9 L528 16 L546 7 L564 12 L582 5 L600 13 L618 9 L638 15 L656 6 L674 12 L692 8 L712 16 L730 7 L748 13 L766 9 L786 15 L804 6 L822 12 L840 8 L860 14 L878 6 L896 13 L914 9 L934 16 L952 7 L970 12 L988 5 L1006 13 L1024 9 L1044 15 L1062 6 L1080 12 L1098 8 L1118 16 L1136 7 L1154 13 L1172 9 L1200 14 L1200 26 Z"/>
    <g id="arrowCircle"><circle cx="7" cy="7" r="7" fill="#fff"/><path d="M5.5 4 L9 7 L5.5 10" stroke="#4a3320" stroke-width="2" fill="none"/></g>
  </defs>
</svg>

<!-- Header -->
<header class="site-header">
  <div class="top-contact" style="left:632px">
    <span class="ico"><svg width="18" height="14" viewBox="0 0 18 14"><rect x="1" y="1" width="16" height="12" rx="1" fill="none" stroke="#fff" stroke-width="1.6"/><path d="M1 2 L9 8 L17 2" stroke="#fff" stroke-width="1.6" fill="none"/></svg></span>
    <div><small>Email Us On:</small><b>hello@loneelmcattle.com</b></div>
  </div>
  <div class="top-contact phone" style="left:888px">
    <span class="ico"><svg width="18" height="18" viewBox="0 0 24 24"><path d="M6.6 10.8a15 15 0 0 0 6.6 6.6l2.2-2.2a1 1 0 0 1 1-.25 11.4 11.4 0 0 0 3.6.6 1 1 0 0 1 1 1V20a1 1 0 0 1-1 1A17 17 0 0 1 3 4a1 1 0 0 1 1-1h3.5a1 1 0 0 1 1 1c0 1.25.2 2.45.6 3.6a1 1 0 0 1-.25 1z" fill="#fff"/></svg></span>
    <div><small>Call Us Today</small><b>+1 555-014-0288</b></div>
  </div>
  <nav class="nav">
    <span class="active">Home</span><span>About</span><span>Cattle Sales</span><span>Bulls</span><span>Cows</span><span>Gallery</span><span>Contact Us</span>
    <svg width="14" height="14" viewBox="0 0 16 16" style="margin-top:2px"><circle cx="6.5" cy="6.5" r="5" stroke="#2b2b2b" stroke-width="2" fill="none"/><path d="M10 10 L15 15" stroke="#2b2b2b" stroke-width="2.4"/></svg>
    <svg width="15" height="14" viewBox="0 0 16 14" style="margin-top:2px"><path d="M0 1 H3 L5 9 H13 L15 3 H4" stroke="#2b2b2b" stroke-width="1.8" fill="#2b2b2b"/><circle cx="6" cy="12" r="1.5" fill="#2b2b2b"/><circle cx="12" cy="12" r="1.5" fill="#2b2b2b"/></svg>
  </nav>
</header>
<div class="logo-disc">
  <span class="brand-dot"></span>
  <span class="brand-text">LONE ELM<br>CATTLE</span>
</div>

<!-- Hero -->
<section class="hero" role="img" aria-label="Highland cattle grazing in a dry pasture with trees under an open sky">
  <h1 class="display">LONE ELM CATTLE</h1>
  <p>Lorem ipsum dolor sit amet, consectetur adipiscing elit, sed do incididunt ut labore et dolore magna aliqua.</p>
  <span class="btn" style="left:496px;top:252px;width:208px;height:55px;font-size:15px">GET STARTED <svg viewBox="0 0 14 14"><use href="#arrowCircle"/></svg></span>
  <svg class="torn" style="bottom:-2px" viewBox="0 0 1200 26" preserveAspectRatio="none"><use href="#tornEdge" fill="#fff"/></svg>
</section>

<!-- About -->
<section class="about">
  <div class="about-mark">
    <span class="brand-dot"></span>
    <span class="brand-text">LONE ELM CATTLE</span>
  </div>
  <h2 class="section-title display">ABOUT US <span class="rule"></span></h2>
  <p style="top:866px">At Lone Elm Cattle, we are dedicated to breeding high-quality cattle that excel in performance, efficiency, and longevity. With years of experience in the industry, we focus on raising superior bulls, heifers, and calves that meet the needs of both commercial and registered cattle operations.</p>
  <p style="top:1006px">Lorem ipsum dolor sit amet, consectetur adipiscing elit, sed do eiusmod tempor incididunt ut labore et dolore magna aliqua. Ut enim ad ut aliquip ex ea commodo consequat.</p>
  <span class="btn" style="left:650px;top:1119px;width:177px;height:48px">READ MORE <svg viewBox="0 0 14 14"><use href="#arrowCircle"/></svg></span>
</section>

<!-- Cattle for sale -->
<section class="sale">
  <svg class="torn" style="top:-24px" viewBox="0 0 1200 26" preserveAspectRatio="none"><use href="#tornEdge" fill="#fdf2e4"/></svg>
  <h2 class="center-title section-title display" style="top:70px">AVAILABLE CATTLE FOR SALE</h2>
  <span class="underline" style="top:126px"></span>

  <div class="card-photo" style="left:111px;background:linear-gradient(180deg,#a9c27a,#6f8f3a 60%,#4f6b2a)" role="img" aria-label="Young highland calf standing in green grass"></div>
  <div class="card-body" style="left:125px"><h3>MR DOMINO K 878</h3><p>DOB 3/23/2023 &nbsp; REG. P44552678 &nbsp; Polled</p></div>
  <span class="btn" style="left:195px;top:477px;width:142px;height:38px;font-size:13px">VIEW DETAILS</span>

  <div class="card-photo" style="left:445px;background:linear-gradient(180deg,#9a8a78,#cfc3b2 50%,#8a7a5c)" role="img" aria-label="White highland cow with long horns by a corral fence"></div>
  <div class="card-body" style="left:459px"><h3>MR DOMINO K 878</h3><p>DOB 3/23/2023 &nbsp; REG. P44552678 &nbsp; Polled</p></div>
  <span class="btn" style="left:529px;top:477px;width:142px;height:38px;font-size:13px">VIEW DETAILS</span>

  <div class="card-photo" style="left:779px;background:linear-gradient(180deg,#b9bcb8,#8c7d5e 45%,#6e5a3a)" role="img" aria-label="Highland cow and calf in a dry paddock"></div>
  <div class="card-body" style="left:793px"><h3>MR DOMINO K 878</h3><p>DOB 3/23/2023 &nbsp; REG. P44552678 &nbsp; Polled</p></div>
  <span class="btn" style="left:863px;top:477px;width:142px;height:38px;font-size:13px">VIEW DETAILS</span>
</section>

<!-- Why choose -->
<section class="why">
  <svg class="torn" style="top:-24px" viewBox="0 0 1200 26" preserveAspectRatio="none"><use href="#tornEdge" fill="#5b3f22"/></svg>
  <h2 class="display">WHY CHOOSE LONE ELM CATTLE</h2>
  <span class="bar"></span>

  <div class="feature" style="top:218px">
    <span class="ico"><svg width="30" height="30" viewBox="0 0 24 24"><path d="M12 2 L20 5 V11 C20 16 16 20 12 22 C8 20 4 16 4 11 V5 Z" fill="none" stroke="#fff" stroke-width="1.5"/><path d="M8 12 L11 15 L16 9" fill="none" stroke="#fff" stroke-width="1.5"/></svg></span>
    <div><h3>Proven Bloodlines</h3><p>We select and breed for genetics that improve weight gain, fertility, and structural soundness.</p></div>
  </div>
  <div class="feature" style="top:328px">
    <span class="ico"><svg width="30" height="30" viewBox="0 0 24 24"><path d="M12 20 C6 15 3 12 3 8.5 A4.5 4.5 0 0 1 12 6 A4.5 4.5 0 0 1 21 8.5 C21 12 18 15 12 20 Z" fill="none" stroke="#fff" stroke-width="1.5"/></svg></span>
    <div><h3>Healthy &amp; Well-Cared-For Cattle</h3><p>We emphasize quality nutrition and health protocols to ensure strong, sound cattle.</p></div>
  </div>
  <div class="feature" style="top:438px">
    <span class="ico"><svg width="30" height="30" viewBox="0 0 24 24"><circle cx="12" cy="12" r="7" fill="none" stroke="#fff" stroke-width="1.5"/><circle cx="12" cy="12" r="3" fill="none" stroke="#fff" stroke-width="1.5"/><path d="M12 2 V5 M12 19 V22 M2 12 H5 M19 12 H22" stroke="#fff" stroke-width="1.5"/></svg></span>
    <div><h3>Customer-Focused Approach</h3><p>We work closely with buyers to help them find the right cattle for their program.</p></div>
  </div>

  <div class="why-photo" role="img" aria-label="Child standing in tall grass beside a fluffy highland calf"></div>
  <svg class="torn" style="bottom:-2px" viewBox="0 0 1200 26" preserveAspectRatio="none"><use href="#tornEdge" fill="#fff"/></svg>
</section>

<!-- Gallery -->
<section class="gallery">
  <h2 class="center-title section-title display" style="top:2600px">OUR GALLERY</h2>
  <span class="underline" style="top:2656px"></span>
  <div class="gallery-tile" style="left:111px;top:2714px;width:483px;height:281px;background:linear-gradient(180deg,#8e8e86,#a58a4f 50%,#c09a45)" role="img" aria-label="Highland cow with horns in a frosty golden field"></div>
  <div class="gallery-tile" style="left:604px;top:2714px;width:484px;height:281px;background:linear-gradient(90deg,#7c8a60,#6b4a2c 45%,#5a3a22 75%,#8a8f6a)" role="img" aria-label="Close view of a shaggy brown highland calf"></div>
  <div class="gallery-tile" style="left:111px;top:3007px;width:322px;height:253px;background:linear-gradient(180deg,#6a6056,#d9d2c6 45%,#b8a98e)" role="img" aria-label="White highland calf eating hay"></div>
  <div class="gallery-tile" style="left:445px;top:3007px;width:310px;height:253px;background:linear-gradient(180deg,#7e8a7a,#7a4a28 45%,#5c3a20)" role="img" aria-label="Brown highland cow resting on the ground"></div>
  <div class="gallery-tile" style="left:767px;top:3007px;width:321px;height:253px;background:linear-gradient(90deg,#c4b08c,#3e4a6a 45%,#6b6a5a 75%,#8a8a7a)" role="img" aria-label="Woman greeting a highland cow up close"></div>
  <span class="btn" style="left:496px;top:3315px;width:208px;height:50px">VIEW ALL GALLERY <svg viewBox="0 0 14 14"><use href="#arrowCircle"/></svg></span>
</section>

<!-- Contact -->
<section class="contact">
  <svg class="torn" style="top:-24px" viewBox="0 0 1200 26" preserveAspectRatio="none"><use href="#tornEdge" fill="#3a2817"/></svg>
  <h2 class="center-title display" style="top:74px">HAVE QUESTION OR MORE INFORMATION</h2>
  <span class="underline" style="top:128px;background:#fff"></span>

  <div class="info" style="top:200px">
    <span class="ico"><svg width="20" height="20" viewBox="0 0 24 24"><path d="M12 22 C7 15 5 12 5 9 A7 7 0 0 1 19 9 C19 12 17 15 12 22 Z" fill="none" stroke="#fff" stroke-width="1.5"/><circle cx="12" cy="9" r="2.5" fill="none" stroke="#fff" stroke-width="1.5"/></svg></span>
    <div><h4>Address</h4><p>1180 Willow Creek Rd., Riverbend, CA, United States,<br>California</p></div>
  </div>
  <div class="info" style="top:302px">
    <span class="ico"><svg width="20" height="20" viewBox="0 0 24 24"><path d="M6.6 10.8a15 15 0 0 0 6.6 6.6l2.2-2.2a1 1 0 0 1 1-.25 11.4 11.4 0 0 0 3.6.6 1 1 0 0 1 1 1V20a1 1 0 0 1-1 1A17 17 0 0 1 3 4a1 1 0 0 1 1-1h3.5a1 1 0 0 1 1 1c0 1.25.2 2.45.6 3.6a1 1 0 0 1-.25 1z" fill="none" stroke="#fff" stroke-width="1.3"/></svg></span>
    <div><h4>Phone Number</h4><p>+1 555-014-0288</p></div>
  </div>
  <div class="info" style="top:382px">
    <span class="ico"><svg width="20" height="16" viewBox="0 0 18 14"><rect x="1" y="1" width="16" height="12" rx="1" fill="none" stroke="#fff" stroke-width="1.3"/><path d="M1 2 L9 8 L17 2" stroke="#fff" stroke-width="1.3" fill="none"/></svg></span>
    <div><h4>Email</h4><p>hello@loneelmcattle.com</p></div>
  </div>

  <div class="field" style="left:565px;top:194px;width:247px;height:42px">&#9786; Name</div>
  <div class="field" style="left:845px;top:194px;width:248px;height:42px">&#9742; Phone Number</div>
  <div class="field" style="left:565px;top:251px;width:247px;height:44px">&#9993; Email Address</div>
  <div class="field" style="left:845px;top:251px;width:248px;height:44px">&#9998; Subject</div>
  <div class="field msg" style="left:565px;top:309px;width:528px;height:85px">&#9993; Messagge</div>
  <span class="btn" style="left:568px;top:426px;width:111px;height:38px;background:#5b3f22">SUBMIT</span>
  <svg class="torn" style="bottom:-2px" viewBox="0 0 1200 26" preserveAspectRatio="none"><use href="#tornEdge" fill="#fff"/></svg>
</section>

<!-- Footer -->
<footer>
  <div class="foot-brand">
    <span class="brand-dot"></span>
    <span class="brand-text">LONE ELM<br>CATTLE</span>
  </div>
  <div class="foot-col" style="left:404px">
    <h4>QUICK LINKS</h4><div class="rule"></div>
    <ul><li>About</li><li>Cattle Sales</li><li>Bulls</li><li>Cows/Heifers</li><li>Gallery</li><li>Contact Us</li></ul>
  </div>
  <div class="foot-col" style="left:580px;width:220px">
    <h4>CONTACT US</h4><div class="rule"></div>
    <div class="fc-row" style="margin-top:18px"><span class="ico"><svg width="12" height="12" viewBox="0 0 24 24"><path d="M6.6 10.8a15 15 0 0 0 6.6 6.6l2.2-2.2a1 1 0 0 1 1-.25 11.4 11.4 0 0 0 3.6.6 1 1 0 0 1 1 1V20a1 1 0 0 1-1 1A17 17 0 0 1 3 4a1 1 0 0 1 1-1h3.5a1 1 0 0 1 1 1c0 1.25.2 2.45.6 3.6a1 1 0 0 1-.25 1z" fill="#fff"/></svg></span><span style="padding-top:3px">+1 555-014-0288</span></div>
    <div class="fc-row"><span class="ico"><svg width="12" height="10" viewBox="0 0 18 14"><rect x="1" y="1" width="16" height="12" fill="#fff"/><path d="M1 2 L9 8 L17 2" stroke="#3a2817" stroke-width="1.6" fill="none"/></svg></span><span style="padding-top:3px">hello@loneelmcattle.com</span></div>
    <div class="fc-row"><span class="ico"><svg width="12" height="12" viewBox="0 0 24 24"><path d="M12 22 C7 15 5 12 5 9 A7 7 0 0 1 19 9 C19 12 17 15 12 22 Z" fill="#fff"/></svg></span><span>1180 Willow Creek Rd., Riverbend, CA, United States, California</span></div>
    <div class="fc-row"><span class="ico"><svg width="12" height="12" viewBox="0 0 24 24"><rect x="4" y="8" width="16" height="12" fill="#fff"/><rect x="7" y="3" width="10" height="6" fill="none" stroke="#fff" stroke-width="2"/></svg></span><span style="padding-top:3px">555-010-7890</span></div>
  </div>
  <div class="foot-col" style="left:831px;width:257px">
    <h4>SUBSCRIBE TO OUR BLOG</h4><div class="rule"></div>
    <p style="font-size:11px;line-height:19px;margin-top:14px;padding-left:6px">Sign up today to get resources on how to attract and retain more customers!</p>
  </div>
  <div class="sub-field">&#9993;&nbsp; Email Address</div>
  <div class="sub-btn"><svg width="16" height="16" viewBox="0 0 24 24"><path d="M2 11 L22 3 L15 21 L11 13 Z" fill="#fff"/></svg></div>
  <span class="social" style="left:834px"></span>
  <span class="social" style="left:872px"></span>
  <span class="social" style="left:910px"></span>
  <span class="social" style="left:950px"></span>
  <span class="chat"><svg width="20" height="18" viewBox="0 0 24 22"><path d="M12 2 C6 2 2 5.5 2 10 C2 12.5 3.3 14.6 5.4 16 L4 20 L9 17.6 C10 17.8 11 18 12 18 C18 18 22 14.5 22 10 C22 5.5 18 2 12 2 Z" fill="#fff"/></svg></span>
  <div class="bottom-bar">
    <span class="left">Copyright© 2025 &nbsp;<u>Lone Elm Cattle</u> &nbsp;| &nbsp;All Rights Reserved</span>
    <span class="right">Terms &amp; Condition &nbsp;| &nbsp;Site Map &nbsp;| &nbsp;Privacy Policy</span>
  </div>
</footer>

</body>
</html>
```